Lawn Maintenance Company needs Flyer (Postcard) Design.

Hi everyone.
The majority of what I do is lawn maintenance (grass cutting and trimming/edging).

I'm pretty well open to anything (even humour) but want to stay away from the cartoon/illustration type flyer (but always receptive if you think you have something that might look good, like Pipwren (Quillbys character) :)
Simple but I guess as everyone, something that catches people's eye.

Feel free to kind of play with the name if you think it would help, I would be willing to pay extra if you thought you had a good idea for some type of logo also.

Flyer/Postcard will be front and back, front mainly outlined here, back would be a list of additional services.

Main points I want to get across.
- Professional
- Reliable
- Not like the larger companies that send students or part time
helpers
Kind of want to get those points across without necessarily saying them.

Ok, well, if you haven't rolled your eyes and headed off to the next project.................... :)

Target Market(s)

Mostly regular people with bungalow / two storey houses that don't want to do it themselves and want a nice lawn to frame their house.

Industry/Entity Type

It Company

Requirements
Must have
• Front
** Brightfield Landscaping and Lawn Services
** Lawn Maintenance
** (416) 555-0382
** brightfieldyards@mailtrove.net

Back
Commercial and Residential
Plaza Maintenance
Spring/Fall Clean-up
Fertilizing
Weed Prevention
Hedge Trimming
Flower Bed Design
Topdressing
Triplemix
Overseeding
Lawn & flower bed re-edging
Eavestrough Cleaning
Nice to have
• ummmm....grass. lol :)
Birds
Butterflies
Should not have
• Elaborate homes/gardens
Pictures/photos of people

**The pictures I have included are to just give you an idea of the work I do and the type of properties I do**
Please let me know if you want more pics.

```html
<!DOCTYPE html>
<html lang="en">
<head>
<meta charset="utf-8">
<title>Brightfield Landscaping and Lawn Services – Postcard</title>
<link rel="stylesheet" href="https://fonts.googleapis.com/css2?family=Kaushan+Script&family=Mulish:wght@700;800&display=swap">
<style>
  :root {
    --sky-deep: #0a34cc;
    --sky-mid: #1f66e6;
    --sky-light: #9fd0f6;
    --horizon: #cfe8c0;
    --grass-light: #a6dc3e;
    --grass-mid: #7cc530;
    --grass-deep: #5aa822;
    --title-yellow: #f6ec52;
    --title-shadow: #1b2a6b;
    --contact-ink: #3d4a2a;
    --list-ink: #ffffff;
    --list-shadow: #0c2460;
    --bullet-petal: #ffffff;
    --bullet-core: #f2c230;
    --page: #ffffff;
  }
  * { margin: 0; padding: 0; box-sizing: border-box; }
  html, body { width: 885px; height: 1200px; overflow: hidden; background: var(--page); }
  .sheet { position: relative; width: 885px; height: 1200px; }

  .card { position: absolute; left: 0; width: 885px; height: 590px; overflow: hidden; }
  .card--front { top: 0; }
  .card--back { top: 610px; }

  .scene {
    position: absolute; inset: 0;
    background: linear-gradient(180deg,
      var(--sky-deep) 0%,
      var(--sky-mid) 38%,
      var(--sky-light) 66%,
      var(--horizon) 72%,
      var(--grass-light) 76%,
      var(--grass-mid) 90%,
      var(--grass-deep) 100%);
  }

  .brand { font-weight: 400; }
  .title {
    position: absolute; font-family: "Kaushan Script", cursive;
    color: var(--title-yellow); font-weight: 400; white-space: nowrap;
    text-shadow: 2px 3px 0 var(--title-shadow), 3px 4px 4px rgba(0,0,0,.35);
  }
  .title--line1 { left: 185px; top: 146px; font-size: 54px; }
  .title--line2 { left: 360px; top: 236px; font-size: 54px; }
  .tagline { left: 198px; top: 302px; font-size: 42px; }

  .contact {
    position: absolute; left: 0; width: 885px; text-align: center;
    font-family: "Mulish", sans-serif; font-weight: 800; color: var(--contact-ink);
    font-size: 17px; line-height: 23px;
  }
  .contact--phone { top: 464px; padding-left: 10px; }
  .contact--email { top: 487px; }
  .contact__icon { display: inline-block; vertical-align: -4px; margin-right: 8px; }

  .services { list-style: none; font-family: "Mulish", sans-serif; font-weight: 800; }
  .services__item {
    position: absolute; white-space: nowrap; font-size: 19.5px; line-height: 24px;
    color: var(--list-ink); text-shadow: 1px 1px 2px var(--list-shadow), 0 0 3px var(--list-shadow);
    display: flex; align-items: center; gap: 8px;
  }
  .services__bullet { flex: none; }
</style>
</head>
<body>
<div class="sheet">

  <section class="card card--front" aria-label="Postcard front">
    <div class="scene" role="img" aria-label="Photo scene: bright blue sky with sun and white clouds, a scarlet macaw in flight, a green lawn meadow with daisies, a red-roofed house on the hill and a monarch butterfly on the grass"></div>

    <h1 class="brand">
      <span class="title title--line1">Brightfield Landscaping</span>
      <span class="title title--line2">and Lawn Services</span>
    </h1>
    <p class="title tagline">Lawn Maintenance</p>

    <p class="contact contact--phone">
      <svg class="contact__icon" width="20" height="20" viewBox="0 0 20 20" aria-hidden="true">
        <circle cx="10" cy="10" r="8.6" fill="none" stroke="currentColor" stroke-width="1.5"/>
        <path d="M7 5.5c-.8.6-1.3 1.6-.7 3 .8 1.9 2.5 3.8 4.4 4.8 1.3.7 2.4.3 3-.5l-1.6-1.5-1.2.6c-1-.5-2-1.6-2.5-2.6l.6-1.2z" fill="currentColor"/>
      </svg>(416) 555-0382
    </p>
    <p class="contact contact--email">brightfieldyards@mailtrove.net</p>
  </section>

  <section class="card card--back" aria-label="Postcard back">
    <div class="scene" role="img" aria-label="Photo scene: bright blue sky with sun and white clouds over a green lawn meadow with daisies, a red-roofed house on the hill and a small orange butterfly"></div>

    <ul class="services">
      <li class="services__item" style="left:64px;top:53px"><svg class="services__bullet" width="14" height="14" viewBox="0 0 14 14" aria-hidden="true"><circle cx="7" cy="7" r="6" fill="var(--bullet-petal)"/><circle cx="7" cy="7" r="3" fill="var(--bullet-core)"/></svg>Commercial and Residential</li>
      <li class="services__item" style="left:116px;top:83px"><svg class="services__bullet" width="14" height="14" viewBox="0 0 14 14" aria-hidden="true"><circle cx="7" cy="7" r="6" fill="var(--bullet-petal)"/><circle cx="7" cy="7" r="3" fill="var(--bullet-core)"/></svg>Plaza Maintenance</li>
      <li class="services__item" style="left:158px;top:113px"><svg class="services__bullet" width="14" height="14" viewBox="0 0 14 14" aria-hidden="true"><circle cx="7" cy="7" r="6" fill="var(--bullet-petal)"/><circle cx="7" cy="7" r="3" fill="var(--bullet-core)"/></svg>Spring/Fall Clean-up</li>
      <li class="services__item" style="left:216px;top:142px"><svg class="services__bullet" width="14" height="14" viewBox="0 0 14 14" aria-hidden="true"><circle cx="7" cy="7" r="6" fill="var(--bullet-petal)"/><circle cx="7" cy="7" r="3" fill="var(--bullet-core)"/></svg>Fertilizing</li>
      <li class="services__item" style="left:262px;top:171px"><svg class="services__bullet" width="14" height="14" viewBox="0 0 14 14" aria-hidden="true"><circle cx="7" cy="7" r="6" fill="var(--bullet-petal)"/><circle cx="7" cy="7" r="3" fill="var(--bullet-core)"/></svg>Weed Prevention</li>
      <li class="services__item" style="left:318px;top:201px"><svg class="services__bullet" width="14" height="14" viewBox="0 0 14 14" aria-hidden="true"><circle cx="7" cy="7" r="6" fill="var(--bullet-petal)"/><circle cx="7" cy="7" r="3" fill="var(--bullet-core)"/></svg>Hedge Trimming</li>
      <li class="services__item" style="left:358px;top:230px"><svg class="services__bullet" width="14" height="14" viewBox="0 0 14 14" aria-hidden="true"><circle cx="7" cy="7" r="6" fill="var(--bullet-petal)"/><circle cx="7" cy="7" r="3" fill="var(--bullet-core)"/></svg>Flower Bed Design</li>
      <li class="services__item" style="left:438px;top:260px"><svg class="services__bullet" width="14" height="14" viewBox="0 0 14 14" aria-hidden="true"><circle cx="7" cy="7" r="6" fill="var(--bullet-petal)"/><circle cx="7" cy="7" r="3" fill="var(--bullet-core)"/></svg>Topdressing</li>
      <li class="services__item" style="left:361px;top:289px"><svg class="services__bullet" width="14" height="14" viewBox="0 0 14 14" aria-hidden="true"><circle cx="7" cy="7" r="6" fill="var(--bullet-petal)"/><circle cx="7" cy="7" r="3" fill="var(--bullet-core)"/></svg>Triplemix</li>
      <li class="services__item" style="left:313px;top:318px"><svg class="services__bullet" width="14" height="14" viewBox="0 0 14 14" aria-hidden="true"><circle cx="7" cy="7" r="6" fill="var(--bullet-petal)"/><circle cx="7" cy="7" r="3" fill="var(--bullet-core)"/></svg>Overseeding</li>
      <li class="services__item" style="left:192px;top:348px"><svg class="services__bullet" width="14" height="14" viewBox="0 0 14 14" aria-hidden="true"><circle cx="7" cy="7" r="6" fill="var(--bullet-petal)"/><circle cx="7" cy="7" r="3" fill="var(--bullet-core)"/></svg>Lawn &amp; flower bed re-edging</li>
      <li class="services__item" style="left:138px;top:377px"><svg class="services__bullet" width="14" height="14" viewBox="0 0 14 14" aria-hidden="true"><circle cx="7" cy="7" r="6" fill="var(--bullet-petal)"/><circle cx="7" cy="7" r="3" fill="var(--bullet-core)"/></svg>Eavestrough Cleaning</li>
    </ul>
  </section>

</div>
</body>
</html>
```